Pricing Poster selling novelty toys and snacks at a Halloween event

I need a poster made for our Halloween event. It would incorporate the items offered and pricing for each.

selling novelty toys and snacks

The Poster needs to say :
PRICE LIST
Bracelets $8 for 1, 4 for $20
Toys $15 for 1, $20 for 2 |
Popcorn $5
Cotton Candy $5
CIDER $4

```html
<!DOCTYPE html>
<html lang="en">
<head>
<meta charset="UTF-8">
<title>Halloween Price List</title>
<link rel="stylesheet" href="https://fonts.googleapis.com/css2?family=Bebas+Neue&family=Creepster&display=swap">
<style>
  :root {
    --night: #150d0b;
    --board: #2c1610;
    --sky-red: #db4427;
    --sky-orange: #ee7f22;
    --moon: #fcc21f;
    --pumpkin: #f28a1f;
    --gold: #f6c431;
    --cream: #fbecc9;
    --rule: #cfc3b4;
  }
  * { margin: 0; padding: 0; box-sizing: border-box; }
  html, body { width: 900px; height: 1200px; overflow: hidden; background: var(--night); }
  .poster {
    position: relative;
    width: 900px;
    height: 1200px;
    background: var(--night);
    font-family: "Bebas Neue", "Oswald", sans-serif;
    color: var(--cream);
  }
  .scene-art {
    position: absolute;
    left: 0; top: 0;
    width: 900px; height: 620px;
    background:
      radial-gradient(ellipse 300px 150px at 450px 335px, rgba(44, 22, 16, 0.97) 0%, rgba(44, 22, 16, 0.92) 55%, rgba(44, 22, 16, 0) 100%),
      linear-gradient(180deg, rgba(21, 13, 11, 0) 0%, rgba(21, 13, 11, 0) 86%, var(--night) 96%),
      radial-gradient(ellipse 260px 220px at 450px 440px, var(--moon) 0%, rgba(252, 194, 31, 0.75) 45%, rgba(252, 194, 31, 0) 100%),
      linear-gradient(180deg, var(--sky-red) 0%, var(--sky-orange) 50%, var(--sky-red) 85%);
  }
  .sign-title {
    position: absolute;
    left: 0; width: 900px;
    text-align: center;
    font-family: "Creepster", cursive;
    line-height: 1;
    transform: rotate(-2deg);
  }
  .sign-title--small { top: 262px; font-size: 48px; color: var(--cream); padding-right: 20px; }
  .sign-title--large { top: 318px; font-size: 84px; color: var(--gold); padding-left: 20px; letter-spacing: 1px; }
  .kicker {
    position: absolute;
    top: 616px; left: 0; width: 900px;
    display: flex; justify-content: center; align-items: center; gap: 14px;
    font-size: 40px; letter-spacing: 1px;
  }
  .kicker::before, .kicker::after {
    content: ""; width: 40px; height: 2px; background: var(--cream);
  }
  .headline {
    position: absolute;
    top: 660px; left: 0; width: 900px;
    text-align: center;
    font-family: "Creepster", cursive;
    font-weight: 400;
    font-size: 92px;
    line-height: 1;
    color: var(--pumpkin);
    letter-spacing: 2px;
  }
  .rule-h { position: absolute; left: 43px; width: 815px; height: 1px; background: var(--rule); }
  .rule-v { position: absolute; width: 1px; background: var(--rule); }
  .item-tag {
    position: absolute;
    height: 54px;
    border: 2.5px solid var(--cream);
    border-radius: 18px;
    display: flex; align-items: center; justify-content: center;
    font-size: 32px; color: var(--pumpkin); letter-spacing: 1px;
  }
  .price-line {
    position: absolute;
    font-size: 42px; line-height: 1; white-space: nowrap; letter-spacing: 1px;
  }
  .price-single {
    position: absolute;
    font-size: 44px; line-height: 1; text-align: center;
  }
</style>
</head>
<body>
<main class="poster">
  <div class="scene-art" role="img" aria-label="Halloween night scene: orange sunset sky with a glowing full moon, bare trees, bats, zombie hands holding a wooden sign, and glowing jack-o'-lantern pumpkins"></div>
  <div class="sign-title sign-title--small">Happy</div>
  <div class="sign-title sign-title--large">Halloween</div>

  <div class="kicker">Special</div>
  <h1 class="headline">Price List</h1>

  <div class="rule-h" style="top:780px"></div>
  <div class="rule-v" style="left:451px; top:805px; height:160px"></div>

  <div class="item-tag" style="left:129px; top:803px; width:236px">Bracelets</div>
  <div class="price-line" style="left:154px; top:868px">$8 FOR .......... 1</div>
  <div class="price-line" style="left:154px; top:925px">$20 FOR ........ 4</div>

  <div class="item-tag" style="left:535px; top:803px; width:237px">Toys</div>
  <div class="price-line" style="left:552px; top:868px">$15 FOR .......... 1</div>
  <div class="price-line" style="left:552px; top:925px">$20 FOR .......... 2</div>

  <div class="rule-h" style="top:988px"></div>
  <div class="rule-v" style="left:281px; top:1006px; height:110px"></div>
  <div class="rule-v" style="left:619px; top:1006px; height:110px"></div>

  <div class="item-tag" style="left:51px; top:1006px; width:192px">Cider</div>
  <div class="price-single" style="left:51px; top:1078px; width:192px">$4</div>

  <div class="item-tag" style="left:319px; top:1006px; width:259px">Cotton Candy</div>
  <div class="price-single" style="left:319px; top:1078px; width:259px">$5</div>

  <div class="item-tag" style="left:658px; top:1006px; width:191px">Popcorn</div>
  <div class="price-single" style="left:658px; top:1078px; width:191px">$5</div>
</main>
</body>
</html>
```